Business Card Design

Business sales of reconditioned / used batteries with mobile delivery and install services. Customers base majority are auto car sales lots and individuals.

Card need to convey quality product reliability and quick prompt professional service.

Card must reflect excellence in customer care and product being offered

Target Market(s)

Auto car lots new and used. Auto repair shops. Individuals.

Industry/Entity Type

Business

Contact Information for Business Card

Batteries Q-Volt
Cars, Trucks, Boats, Motorcycles, lawn mowers, power tools
Delivery & install available most vehicles
Mon-Sat 9-6pm
Dale Morrick 501-738-2056
*product warranty 6 month shelf life battery/1 year blems battery

```html
<!DOCTYPE html>
<html lang="en">
<head>
<meta charset="utf-8">
<title>Batteries Q-Volt – Business Card</title>
<link rel="stylesheet" href="https://fonts.googleapis.com/css2?family=Didact+Gothic&display=swap">
<style>
  :root {
    --card-bg-light: #f7f7f7;
    --card-bg-mid: #e9e9e9;
    --ink: #111111;
    --brand-green: #5ad400;
    --divider: #111111;
  }
  html, body {
    margin: 0;
    padding: 0;
    width: 1200px;
    height: 702px;
    overflow: hidden;
  }
  .card {
    position: relative;
    width: 1200px;
    height: 702px;
    background: linear-gradient(135deg, var(--card-bg-light) 0%, var(--card-bg-mid) 50%, var(--card-bg-light) 100%);
    font-family: "Didact Gothic", sans-serif;
    color: var(--ink);
    text-transform: uppercase;
    overflow: hidden;
  }
  .brand-name {
    position: absolute;
    left: 102px;
    top: 178px;
    margin: 0;
    font-size: 74px;
    font-weight: 400;
    line-height: 78px;
    letter-spacing: 4px;
    color: var(--brand-green);
  }
  .services {
    position: absolute;
    left: 102px;
    top: 352px;
    margin: 0;
    font-size: 35px;
    line-height: 46px;
    letter-spacing: 0.5px;
  }
  .delivery {
    position: absolute;
    left: 102px;
    top: 450px;
    margin: 0;
    font-size: 37px;
    line-height: 46px;
    letter-spacing: 2px;
  }
  .divider {
    position: absolute;
    left: 739px;
    top: 111px;
    width: 4px;
    height: 476px;
    background: var(--divider);
  }
  .contact-icon {
    position: absolute;
    left: 774px;
    fill: var(--ink);
  }
  .icon-person { top: 160px; }
  .icon-phone { top: 312px; }
  .icon-hours { top: 446px; }
  .contact-text {
    position: absolute;
    left: 774px;
    margin: 0;
    font-size: 36px;
    letter-spacing: 1.5px;
    line-height: 1;
  }
  .contact-name { top: 236px; }
  .contact-phone { top: 382px; left: 780px; }
  .contact-hours { top: 529px; left: 780px; }
  .warranty {
    position: absolute;
    left: 0;
    right: 0;
    top: 626px;
    margin: 0;
    text-align: center;
    font-size: 16px;
    letter-spacing: 0.6px;
  }
</style>
</head>
<body>
  <main class="card">
    <h1 class="brand-name">Batteries<br>Q-Volt</h1>

    <p class="services">Cars, Trucks, Boats, Motorcycles,<br>Lawn Mowers, Power Tools</p>
    <p class="delivery">Delivery &amp; Install Available<br>on Most Vehicles</p>

    <div class="divider"></div>

    <svg class="contact-icon icon-person" width="64" height="64" viewBox="0 0 64 64" aria-hidden="true">
      <ellipse cx="32" cy="19" rx="13" ry="16"/>
      <path d="M2 64 C2 46 12 38 22 36 L32 44 L42 36 C52 38 62 46 62 64 Z"/>
    </svg>
    <p class="contact-text contact-name">Dale Morrick</p>

    <svg class="contact-icon icon-phone" width="66" height="56" viewBox="0 0 66 56" aria-hidden="true">
      <path d="M4 14 C4 4 62 4 62 14 L62 20 L48 20 L48 13 L18 13 L18 20 L4 20 Z"/>
      <path d="M20 17 L46 17 L58 40 L58 54 L8 54 L8 40 Z"/>
      <g fill="#f2f2f2">
        <rect x="22" y="28" width="5" height="4"/><rect x="30" y="28" width="5" height="4"/><rect x="38" y="28" width="5" height="4"/>
        <rect x="22" y="35" width="5" height="4"/><rect x="30" y="35" width="5" height="4"/><rect x="38" y="35" width="5" height="4"/>
        <rect x="22" y="42" width="5" height="4"/><rect x="30" y="42" width="5" height="4"/><rect x="38" y="42" width="5" height="4"/>
      </g>
    </svg>
    <p class="contact-text contact-phone">501-738-2056</p>

    <svg class="contact-icon icon-hours" width="62" height="70" viewBox="0 0 62 70" aria-hidden="true">
      <rect x="25" y="0" width="12" height="7"/>
      <rect x="28" y="5" width="6" height="8"/>
      <rect x="49" y="10" width="8" height="6" transform="rotate(45 53 13)"/>
      <rect x="5" y="10" width="8" height="6" transform="rotate(-45 9 13)"/>
      <circle cx="31" cy="40" r="28"/>
      <circle cx="31" cy="40" r="19" fill="#f2f2f2"/>
      <path d="M29 40 L31 26 L33 40 Z"/>
      <circle cx="31" cy="40" r="3"/>
    </svg>
    <p class="contact-text contact-hours">Mon-Sat 9-6pm</p>

    <p class="warranty">*Product warranty 6 month shelf life battery/1 year blems battery</p>
  </main>
</body>
</html>
```